Create a cover for English Grammar Workbook

This book describes a system to learn English in a proper way - we call it The ''VII Arch'' System.

It focuses on not only teaching grammar and its structures, but also giving students tips on how to use it and the best ways to remember what they learn.

The cover should have 3 realistic pillars (3D), with one closer to the front to show that this book is the 1st (front) Pillar.

The title is: "Ways of Conquering Spoken Syntax: *The Simple Path toward Clarity"*

Author's name: Dolan Pritchett

```html
<!DOCTYPE html>
<html lang="en">
<head>
<meta charset="utf-8">
<title>Ways of Conquering Spoken Syntax — Dolan Pritchett</title>
<link rel="stylesheet" href="https://fonts.googleapis.com/css2?family=Libre+Baskerville:wght@400;700&family=Montserrat:wght@600&family=Sacramento&display=swap">
<style>
  :root {
    --backdrop: #ececec;
    --cover: #3a3a3c;
    --accent-red: #d9171d;
    --white: #ffffff;
    --script-grey: #d8d8d8;
    --subtitle-grey: #c4c4c4;
    --pillar-light: #f4f4f4;
    --pillar-mid: #d6d6d6;
    --pillar-shade: #9e9e9e;
  }
  * { box-sizing: border-box; margin: 0; padding: 0; }
  html, body {
    width: 1200px; height: 800px; overflow: hidden;
    background: var(--backdrop);
  }
  .canvas { position: relative; width: 1200px; height: 800px; }
  .book-cover {
    position: absolute; left: 346px; top: 30px;
    width: 508px; height: 740px;
    background: var(--cover);
    overflow: hidden;
  }
  .tagline {
    position: absolute; left: 40px; top: 19px;
    width: 428px; height: 39px;
    border: 3px solid var(--accent-red);
    display: flex; align-items: center; justify-content: center;
    font-family: "Montserrat", sans-serif; font-weight: 600;
    font-size: 16px; letter-spacing: 0.5px;
    color: var(--white); text-transform: uppercase;
    white-space: nowrap;
  }
  .book-title { font-weight: inherit; }
  .title-lead {
    position: absolute; left: 0; right: 0; top: 58px;
    text-align: center;
    font-family: "Sacramento", cursive;
    font-size: 64px; line-height: 72px;
    color: var(--script-grey);
  }
  .title-main {
    position: absolute; left: 50%; top: 150px;
    transform: translateX(-50%);
    background: var(--accent-red);
    padding: 6px 14px 4px;
    font-family: "Libre Baskerville", serif; font-weight: 700;
    font-size: 42px; line-height: 56px;
    color: var(--white); text-align: center;
    text-transform: uppercase; white-space: nowrap;
    letter-spacing: 1px;
  }
  .title-sub {
    position: absolute; left: 0; right: 0; top: 278px;
    text-align: center;
    font-family: "Libre Baskerville", serif; font-weight: 700;
    font-size: 42px; line-height: 50px; letter-spacing: 6px;
    color: var(--subtitle-grey); text-transform: uppercase;
  }
  .pillars-art {
    position: absolute; left: 0; top: 330px;
    width: 508px; height: 350px;
  }
  .author-band {
    position: absolute; left: 0; right: 0; bottom: 0;
    height: 58px; background: var(--accent-red);
    display: flex; align-items: center; justify-content: center;
    font-family: "Libre Baskerville", serif; font-weight: 700;
    font-size: 22px; letter-spacing: 6px;
    color: var(--white); text-transform: uppercase;
  }
</style>
</head>
<body>
<main class="canvas">
  <section class="book-cover">
    <div class="tagline">The Simple Path toward Clarity</div>
    <h1 class="book-title">
      <span class="title-lead">Ways of</span>
      <span class="title-main">Conquering<br>Spoken</span>
      <span class="title-sub">Syntax</span>
    </h1>
    <svg class="pillars-art" viewBox="0 0 508 350" role="img" aria-label="Three white Ionic columns, the middle one larger and standing closer to the front">
      <defs>
        <linearGradient id="pillar-tone" x1="0" y1="0" x2="1" y2="0">
          <stop offset="0" stop-color="var(--pillar-shade)"/>
          <stop offset="0.45" stop-color="var(--pillar-light)"/>
          <stop offset="1" stop-color="var(--pillar-mid)"/>
        </linearGradient>
      </defs>
      <rect class="pillar-side" x="30" y="60" width="115" height="261" rx="4" fill="url(#pillar-tone)"/>
      <rect class="pillar-front" x="179" y="9" width="142" height="332" rx="4" fill="url(#pillar-tone)"/>
      <rect class="pillar-side" x="362" y="60" width="113" height="261" rx="4" fill="url(#pillar-tone)"/>
    </svg>
    <div class="author-band">Dolan Pritchett</div>
  </section>
</main>
</body>
</html>
```